Brick pressure cleaning business needs business cards that are memorable

The business is called Kestrel hydroblast brick and pressure cleaning.
we blast bricks on new houses and driveways. I would like a logo with water spraying out of the letter s in the wording. Also bricks on the card somehow and maybe the word kestrel to be on an angle above the rest of the business name if possible. some shinny gold would be nice somewhere to. Would like to list our services on the back of card- red and cream brick clean, green stain removal, floor scrapes, fence panel clean or changeout. Driveway cleans. hard surface pressure cleans.

Target Market(s)

Building companies and home reno people

Industry/Entity Type

construction

Contact Information for Business Card

business name,phone,number my name, services on the back

Colors
0054AA
0677BA
7BADD7
CADEEF
E8F1F8
FFF300
FFF600
FEFA6F
FFFEC7
FFFEE8

```html
<!DOCTYPE html>
<html lang="en">
<head>
<meta charset="utf-8">
<title>Kestrel Hydroblast Business Card</title>
<link href="https://fonts.googleapis.com/css2?family=Kumbh+Sans:wght@400;500;700&display=swap" rel="stylesheet">
<style>
  :root {
    --backdrop: #d6d6d6;
    --card: #0a0c0c;
    --ink: #ffffff;
    --gold: #e2b52f;
    --gold-light: #fbe97a;
    --gold-deep: #c8901e;
  }
  * { box-sizing: border-box; margin: 0; padding: 0; }
  html, body {
    width: 1200px; height: 1200px; overflow: hidden;
    background: var(--backdrop);
    font-family: "Kumbh Sans", "Helvetica Neue", Arial, sans-serif;
  }
  .card {
    position: absolute;
    background: var(--card);
    color: var(--ink);
  }
  .card--front { left: 261px; top: 117px; width: 699px; height: 399px; }
  .card--back  { left: 259px; top: 652px; width: 709px; height: 406px; }

  .gold-band {
    position: absolute; left: 0; right: 0; height: 12px;
    background: linear-gradient(90deg, var(--gold-light), var(--gold-deep) 45%, var(--gold-light) 100%);
  }
  .card--front .gold-band { top: 359px; }
  .card--back .gold-band { top: 228px; }

  .brand {
    position: absolute;
    display: flex; align-items: center; gap: 16px;
    color: var(--gold);
    font-weight: 700;
    text-transform: uppercase;
  }
  .brand__mark { flex: none; background: var(--gold); }
  .brand__name { line-height: 1.15; letter-spacing: 0.04em; }
  .card--front .brand { left: 39px; top: 60px; width: 360px; }
  .card--front .brand__mark { width: 64px; height: 64px; }
  .card--front .brand__name { font-size: 23px; }
  .card--back .brand { left: 144px; top: 70px; width: 440px; }
  .card--back .brand__mark { width: 84px; height: 84px; }
  .card--back .brand__name { font-size: 29px; }

  .contact { position: absolute; left: 34px; top: 219px; list-style: none; }
  .contact__item {
    display: flex; align-items: center; gap: 10px;
    font-size: 16px; font-weight: 500; letter-spacing: 0.03em;
    height: 29px;
  }
  .contact__icon { width: 14px; height: 14px; fill: var(--gold); flex: none; }

  .person { position: absolute; left: 442px; top: 248px; }
  .person__name { font-size: 38px; font-weight: 700; letter-spacing: 0.01em; line-height: 1; }
  .person__role { color: var(--gold); font-size: 21px; font-weight: 400; letter-spacing: 0.08em; margin-top: 8px; }

  .services { position: absolute; list-style: none; font-size: 17px; font-weight: 500; letter-spacing: 0.03em; }
  .services li { position: relative; padding-left: 16px; line-height: 22px; }
  .services li::before {
    content: ""; position: absolute; left: 0; top: 9px;
    width: 5px; height: 5px; border-radius: 50%; background: var(--ink);
  }
  .services--left { left: 116px; top: 266px; }
  .services--left li { margin-bottom: 0.5px; }
  .services--right { left: 455px; top: 287px; }
</style>
</head>
<body>

<section class="card card--front" aria-label="Business card front">
  <div class="brand">
    <span class="brand__mark"></span>
    <span class="brand__name">Kestrel hydroblast brick and pressure cleaning</span>
  </div>

  <ul class="contact">
    <li class="contact__item">
      <svg class="contact__icon" viewBox="0 0 24 24"><path d="M6.6 10.8a15.2 15.2 0 0 0 6.6 6.6l2.2-2.2a1 1 0 0 1 1-.25 11.4 11.4 0 0 0 3.6.57 1 1 0 0 1 1 1V20a1 1 0 0 1-1 1A17 17 0 0 1 3 4a1 1 0 0 1 1-1h3.5a1 1 0 0 1 1 1c0 1.25.2 2.45.57 3.57a1 1 0 0 1-.25 1z"/></svg>
      040 555 0192
    </li>
    <li class="contact__item">
      <svg class="contact__icon" viewBox="0 0 24 24"><path d="M2 5h20v14H2z M3 6l9 7 9-7" fill="none" stroke="#e2b52f" stroke-width="2"/></svg>
      kestrelbrickclean@mailbox.com
    </li>
    <li class="contact__item">
      <svg class="contact__icon" viewBox="0 0 24 24"><path d="M12 2 4 5v6c0 5 3.4 9.6 8 11 4.6-1.4 8-6 8-11V5z"/></svg>
      abn number 41 000 555 217
    </li>
  </ul>

  <div class="person">
    <p class="person__name">Dale Merrin</p>
    <p class="person__role">DIRECTOR</p>
  </div>

  <div class="gold-band"></div>
</section>

<section class="card card--back" aria-label="Business card back">
  <div class="brand">
    <span class="brand__mark"></span>
    <span class="brand__name">Kestrel hydroblast brick and pressure cleaning</span>
  </div>

  <div class="gold-band"></div>

  <ul class="services services--left">
    <li>Garden Kerbing</li>
    <li>Red and Cream Brick Clean</li>
    <li>Hard Surface Pressure Cleans</li>
    <li>Fence Panel Cleans or Changeout</li>
  </ul>
  <ul class="services services--right">
    <li>Floor Scrapes</li>
    <li>Driveway Cleans</li>
    <li>Green Stain Removal</li>
  </ul>
</section>

</body>
</html>
```